Eye catching Stationary Design

Healthcare consultant firm looking for stationary design ( letterhead, envelope and business cards) That’s professional, classy and eye catching . The design should incorporate the logo and the colors of the logo in its design. You can see the logo on our website at www crestmore advisory. net.

```html
<!DOCTYPE html>
<html lang="en">
<head>
<meta charset="utf-8">
<title>Crestmore Advisory – Stationery Set</title>
<link href="https://fonts.googleapis.com/css2?family=Montserrat:wght@400;500;600;700&display=swap" rel="stylesheet">
<style>
  :root{
    --backdrop:#323b3e;
    --paper:#ffffff;
    --mist-light:#f7f7f7;
    --mist-dark:#e6e7e8;
    --sky:#4cd3ef;
    --royal:#0d47f0;
    --ink:#1d1d1f;
    --brand-ink:#2a2f3a;
  }
  *{box-sizing:border-box;margin:0;padding:0}
  html,body{width:1200px;height:780px;overflow:hidden}
  body{background:var(--backdrop);font-family:"Montserrat",sans-serif;position:relative;color:var(--ink)}
  .sheet{position:absolute;background:var(--paper);overflow:hidden;box-shadow:0 2px 6px rgba(0,0,0,.35)}
  .wave{position:absolute;left:0;width:100%;display:block}
  .brand-name{font-family:"Montserrat",sans-serif;font-weight:600;color:var(--brand-ink);letter-spacing:.04em;text-transform:uppercase;white-space:nowrap}

  /* Letterhead */
  .letterhead{left:98px;top:116px;width:432px;height:560px}
  .letterhead .head-band{position:absolute;left:0;top:0;width:100%;height:186px;background:linear-gradient(var(--mist-light),var(--mist-dark))}
  .letterhead .foot-band{position:absolute;left:0;top:371px;width:100%;height:189px;background:linear-gradient(var(--mist-dark),#fafafa 80%)}
  .letterhead .brand-name{position:absolute;left:14px;top:52px;font-size:15px}
  .contact-list{position:absolute;left:257px;top:22px;list-style:none;font-size:10px;font-weight:500;line-height:14px}
  .contact-list li{display:flex;align-items:flex-start;gap:6px;margin-bottom:0}
  .contact-list svg{flex:none;width:7px;height:7px;margin-top:3.5px}
  .letterhead .wave{top:490px;height:70px}
  .footer-email{position:absolute;left:0;width:100%;text-align:center;color:#fff;font-weight:500}
  .letterhead .footer-email{top:536px;font-size:10.5px}

  /* Business card front */
  .card{top:111px;width:216px;height:122px}
  .card-front{left:625px}
  .card-front .brand-name{position:absolute;left:0;width:100%;text-align:center;top:52px;font-size:8.5px}
  .card-front .wave{top:74px;height:48px}
  .card-front .footer-email{top:93px;font-size:5px}

  /* Business card back */
  .card-back{left:881px}
  .card-back .side-wave{position:absolute;inset:0;width:100%;height:100%}
  .card-back .brand-name{position:absolute;left:6px;top:53px;font-size:5px}
  .holder{position:absolute;left:105px;top:16px;color:#fff}
  .holder-name{font-size:8px;font-weight:700;letter-spacing:.02em}
  .holder-role{font-size:6.5px;font-weight:600;color:var(--royal);margin-top:0}
  .card-back .contact-list{left:100px;top:51px;font-size:4.6px;line-height:6.4px;color:var(--ink)}
  .card-back .contact-list li{gap:3px}
  .card-back .contact-list svg{width:4px;height:4px;margin-top:1px}

  /* Envelope front */
  .envelope-front{left:629px;top:252px;width:466px;height:202px}
  .envelope-front .brand-name{position:absolute;left:22px;top:108px;font-size:8.5px}
  .envelope-front .wave{top:132px;height:70px}
  .envelope-front .footer-email{top:172px;font-size:12px}

  /* Envelope back */
  .envelope-back{left:627px;top:473px;width:469px;height:204px}
  .envelope-back .flap{position:absolute;left:0;top:0;width:100%;height:70px}
</style>
</head>
<body>

<!-- Letterhead -->
<section class="sheet letterhead">
  <div class="head-band"></div>
  <div class="foot-band"></div>
  <p class="brand-name">Crestmore Advisory LLC</p>
  <ul class="contact-list">
    <li><svg viewBox="0 0 10 10"><path d="M1 4 Q5 0 9 4 L8 5 L6.5 4 V3 H3.5 V4 L2 5 Z M2.5 6 H7.5 V9 H2.5 Z" fill="var(--royal)"/></svg>(555) 214-0387</li>
    <li><svg viewBox="0 0 10 10"><circle cx="5" cy="5" r="4.2" fill="none" stroke="var(--royal)" stroke-width="1"/><path d="M1 5 H9 M5 1 V9 M2 3 H8 M2 7 H8" stroke="var(--royal)" stroke-width=".7"/></svg>info@crestmoreadvisory.net</li>
    <li><svg viewBox="0 0 10 10"><path d="M5 10 L2 5 A3.2 3.2 0 1 1 8 5 Z" fill="var(--royal)"/><circle cx="5" cy="3.6" r="1.2" fill="#fff"/></svg>418 Harlow St Suite 12,<br>Brookfield, NY 10090, USA</li>
  </ul>
  <svg class="wave" viewBox="0 0 858 140" preserveAspectRatio="none" aria-hidden="true">
    <path d="M0 0 Q429 120 858 0 V140 H0 Z" fill="var(--sky)"/>
    <path d="M0 0 Q429 95 858 0 Q429 160 0 0 Z" fill="var(--royal)"/>
    <circle cx="429" cy="64" r="10" fill="var(--royal)" stroke="#fff" stroke-width="2"/>
    <path d="M419 64 H439 M429 54 V74" stroke="#fff" stroke-width="1.4"/>
  </svg>
  <p class="footer-email">info@crestmoreadvisory.net</p>
</section>

<!-- Business card front -->
<section class="sheet card card-front">
  <p class="brand-name">Crestmore Advisory LLC</p>
  <svg class="wave" viewBox="0 0 428 96" preserveAspectRatio="none" aria-hidden="true">
    <path d="M0 0 Q214 56 428 0 V96 H0 Z" fill="var(--sky)"/>
    <path d="M0 0 Q214 44 428 0 Q214 72 0 0 Z" fill="var(--royal)"/>
    <circle cx="214" cy="32" r="5" fill="var(--royal)" stroke="#fff" stroke-width="1.2"/>
  </svg>
  <p class="footer-email">info@crestmoreadvisory.net</p>
</section>

<!-- Business card back -->
<section class="sheet card card-back">
  <svg class="side-wave" viewBox="0 0 428 243" preserveAspectRatio="none" aria-hidden="true">
    <path d="M150 0 Q230 121 150 243 H428 V0 Z" fill="var(--royal)"/>
    <path d="M168 0 Q238 121 168 243 H428 V0 Z" fill="var(--sky)"/>
  </svg>
  <p class="brand-name">Crestmore Advisory LLC</p>
  <div class="holder">
    <p class="holder-name">MARCUS ELLERY</p>
    <p class="holder-role">DIRECTOR</p>
  </div>
  <ul class="contact-list">
    <li><svg viewBox="0 0 10 10"><circle cx="5" cy="5" r="5" fill="var(--royal)"/></svg>(555) 214-0387</li>
    <li><svg viewBox="0 0 10 10"><circle cx="5" cy="5" r="5" fill="var(--royal)"/></svg>info@crestmoreadvisory.net</li>
    <li><svg viewBox="0 0 10 10"><path d="M5 10 L2 5 A3.2 3.2 0 1 1 8 5 Z" fill="var(--royal)"/></svg>418 Harlow St Suite 12,<br>Brookfield, NY 10090, USA</li>
  </ul>
</section>

<!-- Envelope front -->
<section class="sheet envelope-front">
  <p class="brand-name">Crestmore Advisory LLC</p>
  <svg class="wave" viewBox="0 0 925 140" preserveAspectRatio="none" aria-hidden="true">
    <path d="M0 0 Q462 120 925 0 V140 H0 Z" fill="var(--sky)"/>
    <path d="M0 0 Q462 95 925 0 Q462 160 0 0 Z" fill="var(--royal)"/>
    <circle cx="462" cy="68" r="10" fill="var(--royal)" stroke="#fff" stroke-width="2"/>
    <path d="M452 68 H472 M462 58 V78" stroke="#fff" stroke-width="1.4"/>
  </svg>
  <p class="footer-email">info@crestmoreadvisory.net</p>
</section>

<!-- Envelope back -->
<section class="sheet envelope-back">
  <svg class="flap" viewBox="0 0 930 124" preserveAspectRatio="none" aria-hidden="true">
    <path d="M0 0 H930 L880 103 Q862 124 830 124 H100 Q68 124 50 103 Z" fill="var(--sky)"/>
  </svg>
</section>

</body>
</html>
```